Visitenkarte erstellen für Reiki Praxis

Visitenkarten für Reiki Praxis Doppelseitig

business cards reiki practice double-sided

The background can also be a different color

```html
<!DOCTYPE html>
<html lang="en">
<head>
<meta charset="utf-8">
<title>Lumen Balance – Business Cards</title>
<link rel="stylesheet" href="https://fonts.googleapis.com/css2?family=Open+Sans:wght@400;600;700&display=swap">
<style>
  :root {
    --bg: #c9c9c9;
    --card: #1c1c1c;
    --white: #ffffff;
    --gold: #e6a823;
    --rose: #d98aa8;
    --peach: #f2b985;
  }
  * { box-sizing: border-box; margin: 0; padding: 0; }
  html, body { width: 1200px; height: 788px; overflow: hidden; }
  body {
    background: var(--bg);
    font-family: "Open Sans", Arial, sans-serif;
    position: relative;
  }
  .card {
    position: absolute;
    top: 239px;
    width: 540px;
    height: 310px;
    background: var(--card);
    border-radius: 22px;
    box-shadow: 0 10px 26px rgba(0,0,0,.28);
    overflow: hidden;
  }
  .card--info { left: 40px; }
  .card--brand { left: 620px; }

  /* Info side */
  .wordmark {
    position: absolute;
    display: flex;
    align-items: center;
    gap: 10px;
    color: var(--white);
    font-weight: 400;
    letter-spacing: 1px;
  }
  .card--info .wordmark { left: 38px; top: 42px; font-size: 24px; }
  .wordmark__dot {
    width: 14px; height: 14px; border-radius: 50%;
    background: var(--peach);
  }
  .person {
    position: absolute;
    left: 38px; top: 120px;
    padding-left: 18px;
  }
  .person__swatch {
    position: absolute;
    left: 0; top: 4px;
    width: 8px; height: 42px;
    background: linear-gradient(180deg, var(--rose), var(--peach));
  }
  .person__name {
    color: var(--gold);
    font-weight: 700;
    font-size: 22px;
    letter-spacing: .5px;
    line-height: 1.1;
  }
  .person__role {
    color: var(--white);
    font-size: 14px;
    margin-top: 3px;
  }
  .contacts {
    position: absolute;
    left: 38px; top: 196px;
    list-style: none;
  }
  .contacts li {
    display: flex;
    align-items: center;
    gap: 9px;
    color: var(--white);
    font-size: 14px;
    line-height: 26px;
  }
  .contacts svg { width: 13px; height: 13px; fill: var(--gold); flex: none; }

  /* Brand side */
  .card--brand .brand-block {
    position: absolute;
    inset: 0;
    display: flex;
    flex-direction: column;
    align-items: center;
    justify-content: center;
    gap: 18px;
  }
  .brand-block__dot {
    width: 30px; height: 30px; border-radius: 50%;
    background: linear-gradient(135deg, var(--rose), var(--peach));
  }
  .brand-block__name {
    color: var(--white);
    font-size: 38px;
    font-weight: 400;
    letter-spacing: 1.5px;
  }
</style>
</head>
<body>
  <section class="card card--info" aria-label="Business card, contact side">
    <div class="wordmark"><span class="wordmark__dot"></span>LUMEN BALANCE</div>
    <div class="person">
      <span class="person__swatch"></span>
      <p class="person__name">CLARA WINTER</p>
      <p class="person__role">Founder/CEO</p>
    </div>
    <ul class="contacts">
      <li>
        <svg viewBox="0 0 24 24" aria-hidden="true"><path d="M6.6 10.8a15.1 15.1 0 0 0 6.6 6.6l2.2-2.2a1 1 0 0 1 1-.25 11.4 11.4 0 0 0 3.6.57 1 1 0 0 1 1 1V20a1 1 0 0 1-1 1A17 17 0 0 1 3 4a1 1 0 0 1 1-1h3.5a1 1 0 0 1 1 1c0 1.25.2 2.45.57 3.57a1 1 0 0 1-.25 1z"/></svg>
        (555) 210 4836
      </li>
      <li>
        <svg viewBox="0 0 24 24" aria-hidden="true"><path d="M2 5h20v14H2z M2 5l10 8 10-8" fill="none" stroke="#e6a823" stroke-width="2.4"/></svg>
        info@lumenbalance.com
      </li>
      <li>
        <svg viewBox="0 0 24 24" aria-hidden="true"><circle cx="12" cy="12" r="10" fill="none" stroke="#e6a823" stroke-width="2.2"/><path d="M2 12h20M12 2c3 3 3 17 0 20M12 2c-3 3-3 17 0 20" fill="none" stroke="#e6a823" stroke-width="1.8"/></svg>
        www.lumenbalance.com
      </li>
    </ul>
  </section>

  <section class="card card--brand" aria-label="Business card, brand side">
    <div class="brand-block">
      <span class="brand-block__dot"></span>
      <p class="brand-block__name">LUMEN BALANCE</p>
    </div>
  </section>
</body>
</html>
```